Letter Head Design - Finance industry

Design a letterhead to match the logo. Needs to be clean, simple and crisp. I'm open to suggestions. Will be using the logo that was submitted last with the W crossed over

Target Market(s)

Small medium businesses and government department's

Industry/Entity Type

Industry

Font styles to use
Sans Serif

Colors
cadf82
bcd85c
acd036
9bcb3c
e9e9e9
aaaaaa
000000
7f7f7f
b7b7b7

Requirements
Must have
• Need to display: Logo, Business address, ABN number, ASIC register number, contact phone, website, company email. Details are as per below:

Suite 4B Level 17
Marlowe Harbour Tower
9 Tindall Place
Sydney NSW 2000
Landline Ph: 02 5193 2604
Ph: 1300 4917 63
Email: enquiries@brightmoorfin.com.au
W: www.brightmoorfin.com.au

On the footer, the details below need to be specified:
ABN: 43 719 385 207
ASIC Registration Number: 27 318640571

Should not have
• No imagery or design that is not in line with the logo

```html
<!DOCTYPE html>
<html lang="en">
<head>
<meta charset="utf-8">
<title>Brightmoor Finance – Letterhead</title>
<link href="https://fonts.googleapis.com/css2?family=Questrial&display=swap" rel="stylesheet">
<style>
  :root{
    --green:#a8c83e;
    --green-light:#cadf82;
    --black:#000000;
    --grey:#7f7f7f;
    --white:#ffffff;
    --backdrop:#e9e9e9;
  }
  *{box-sizing:border-box;margin:0;padding:0}
  html,body{width:1200px;height:1001px;overflow:hidden}
  body{
    background:var(--backdrop);
    font-family:"Questrial",sans-serif;
    position:relative;
  }
  .page{
    position:absolute;top:88px;width:584px;height:824px;
    box-shadow:0 2px 10px rgba(0,0,0,.18);
  }
  .letterhead{left:17px;background:var(--white)}
  .cover{left:601px;background:var(--green)}

  .brand{position:absolute;display:flex;align-items:center;gap:8px}
  .brand-dot{width:14px;height:14px;border-radius:50%;flex:none}
  .brand-name{font-size:24px;line-height:25px;letter-spacing:.2px}
  .letterhead .brand{left:40px;top:52px}
  .letterhead .brand-dot{background:var(--green)}
  .letterhead .brand-name{color:var(--grey)}
  .cover .brand{left:228px;top:374px}
  .cover .brand-dot{background:var(--white)}
  .cover .brand-name{color:var(--white);font-size:26px;line-height:27px}

  .address{
    position:absolute;right:44px;top:78px;
    text-align:right;font-size:10px;line-height:12px;color:var(--black);
  }
  .address svg{vertical-align:-1px;margin-right:3px}

  .footer-band{
    position:absolute;left:0;right:0;bottom:0;height:26px;
    background:var(--green);color:var(--white);
    display:flex;align-items:center;padding:0 6px 0 14px;
    font-size:7.5px;gap:0;
  }
  .footer-item{display:flex;align-items:center;gap:4px}
  .footer-item svg{flex:none}
  .sep{margin:0 10px;opacity:.8}
  .registration{
    margin-left:auto;text-align:right;font-size:5.5px;line-height:7px;
  }
</style>
</head>
<body>
  <section class="page letterhead">
    <div class="brand">
      <span class="brand-dot"></span>
      <span class="brand-name">Brightmoor<br>Finance</span>
    </div>

    <address class="address" style="font-style:normal">
      <svg width="7" height="9" viewBox="0 0 7 9" aria-hidden="true"><path d="M3.5 0A3.5 3.5 0 0 0 0 3.5C0 6 3.5 9 3.5 9S7 6 7 3.5A3.5 3.5 0 0 0 3.5 0Zm0 5A1.5 1.5 0 1 1 3.5 2a1.5 1.5 0 0 1 0 3Z" fill="#a8c83e"/></svg>Suite 4B Level 17,<br>
      Marlowe Harbour Tower,<br>
      9 Tindall Place, Sydney NSW 2000
    </address>

    <footer class="footer-band">
      <span class="footer-item">
        <svg width="7" height="7" viewBox="0 0 10 10" aria-hidden="true"><circle cx="5" cy="5" r="4.2" fill="none" stroke="#fff" stroke-width="1.2"/><path d="M1 5h8M5 1c-2 2.5-2 5.5 0 8M5 1c2 2.5 2 5.5 0 8" fill="none" stroke="#fff" stroke-width=".8"/></svg>
        www.brightmoorfin.com.au
      </span>
      <span class="sep">|</span>
      <span class="footer-item">
        <svg width="8" height="6" viewBox="0 0 10 7" aria-hidden="true"><rect x=".5" y=".5" width="9" height="6" fill="none" stroke="#fff"/><path d="M.5.5 5 4 9.5.5" fill="none" stroke="#fff"/></svg>
        enquiries@brightmoorfin.com.au
      </span>
      <span class="sep">|</span>
      <span class="footer-item">
        <svg width="6" height="8" viewBox="0 0 6 9" aria-hidden="true"><rect x=".5" y=".5" width="5" height="8" rx="1" fill="none" stroke="#fff"/></svg>
        02 5193 2604
      </span>
      <span class="sep">|</span>
      <span class="footer-item">
        <svg width="6" height="8" viewBox="0 0 6 9" aria-hidden="true"><rect x=".5" y=".5" width="5" height="8" rx="1" fill="none" stroke="#fff"/></svg>
        1300 4917 63
      </span>
      <span class="sep">|</span>
      <span class="registration">
        ABN: 43 719 385 207<br>
        ASIC Registration Number: 27 318640571
      </span>
    </footer>
  </section>

  <section class="page cover">
    <div class="brand">
      <span class="brand-dot"></span>
      <span class="brand-name">Brightmoor<br>Finance</span>
    </div>
  </section>
</body>
</html>
```